New Business and Accounting Software need a Web Site

The website is for a Business and Accounting Software that has 8 products.
Each product has its owns logo and color, when you do the design have in consideration that we are looking the experience that when you change from one product page to another the look and feel adjust to the color and logo of the product.
The product are:
Ventas (Sales)
Compras (Purchases)
Contabilidad (Accounting)
Presupuesto (Budget)
Inventarios (Inventory)
Bancos (Banks)
NĂ³mina RH (Human Resources Payroll)
CRM (Customer Relationship Manager)

You can see how the main logo and variations are used in each page
- https://www.vemu.com/
- https://www.lari.com/
- https://www.tovimal.com/

Our goal is to be similar to them.

I have created a word document to explain what I want.
You need to design:
1 Home Page
1 Product Landing Page
1 Product Detail Page
1 Price Page

I am attaching:
1. Main Logo
2. 8 Product Logos
3. Website Idea, you can create your own idea.

You are welcome to use other icons for the each product if you want.

Independet professionals and Small and Medium Companies

Business and Accounting Software

Coded - Design and coding required

0054AA
0677BA
7BADD7
CADEEF
E8F1F8

• Must show all products in the main page

```html
<!DOCTYPE html>
<html lang="en">
<head>
<meta charset="utf-8">
<title>Nubecta — Platform to run your business</title>
<link href="https://fonts.googleapis.com/css2?family=Poppins:wght@400;500;600;700&display=swap" rel="stylesheet">
<style>
:root{
  --blue-dark:#0054AA;
  --blue:#0677BA;
  --blue-mid:#6497C7;
  --blue-light:#7BADD7;
  --blue-pale:#CADEEF;
  --blue-mist:#E8F1F8;
  --ink:#1d1d1f;
  --text:#4a4a55;
  --white:#fff;
}
*{box-sizing:border-box;margin:0;padding:0}
html,body{width:1200px;height:4677px;overflow:hidden}
body{position:relative;font-family:'Poppins',sans-serif;color:var(--ink);background:var(--white)}
.abs{position:absolute}
a{color:inherit;text-decoration:none}
.btn{position:absolute;display:flex;align-items:center;justify-content:center;border-radius:30px;font-weight:500;color:var(--white)}
/* nav */
.brand{display:flex;align-items:center;gap:10px;font-weight:600;font-size:38px;color:var(--blue-dark)}
.brand-dot{width:44px;height:44px;border-radius:50%;background:var(--blue-dark)}
.nav a{position:absolute;top:36px;font-size:16px;color:var(--ink)}
.nav a.active{color:var(--blue-dark)}
/* hero */
.hero-photo{left:0;top:94px;width:1200px;height:614px;background:linear-gradient(110deg,#c9d4df 0%,#dfe6ee 40%,#eef2f6 70%,#e3e8ee 100%);clip-path:polygon(0 0,100% 0,100% 73%,0 100%)}
.hero-kicker{left:93px;top:258px;font-size:23px;letter-spacing:5px;font-weight:500}
.hero-title{left:93px;top:290px;font-size:52px;line-height:62px;font-weight:600;color:var(--blue-dark)}
/* section titles */
.sec-title{left:0;width:1200px;text-align:center;font-size:37px;font-weight:600}
.sec-title span{color:var(--blue-dark)}
/* apps */
.app{position:absolute;width:226px;height:94px;border:2px solid;border-radius:6px;display:flex;flex-direction:column;align-items:center;justify-content:center;gap:6px;font-weight:600;font-size:17px;letter-spacing:.5px}
.app i{display:block;width:34px;height:30px;border-radius:5px}
/* profile */
.profile-band{left:0;top:1207px;width:1200px;height:1209px;background:var(--blue-mid);clip-path:polygon(0 42px,100% 0,100% 100%,0 100%)}
.hex{position:absolute;width:382px;height:330px;background:var(--white);clip-path:polygon(25% 0,75% 0,100% 50%,75% 100%,25% 100%,0 50%);text-align:center;padding:40px 62px 0}
.hex h3{font-size:22px;font-weight:500;margin-bottom:12px}
.hex p{font-size:15px;line-height:28.5px;color:var(--text)}
.hex a{display:inline-block;margin-top:12px;font-size:15px;font-weight:500;color:var(--blue-dark)}
.mini-hex{position:absolute;clip-path:polygon(25% 0,75% 0,100% 50%,75% 100%,25% 100%,0 50%)}
/* features */
.tabs{left:93px;top:2605px;width:1013px;height:100px;background:var(--white);box-shadow:0 6px 24px rgba(0,84,170,.12);display:flex}
.tab{flex:1;padding:28px 0 0 26px;font-size:15px;font-weight:500;position:relative}
.tab i{display:block;width:16px;height:18px;border-radius:3px;background:var(--blue-light);margin-bottom:10px}
.tab.active{color:var(--blue-dark)}
.tab.active i{background:var(--blue-dark);border-radius:50%}
.tab.active::after{content:"";position:absolute;left:0;bottom:0;width:218px;height:3px;background:var(--blue-dark)}
.feature-title{left:679px;top:2806px;font-size:39px;line-height:44px;font-weight:600}
.feature-title span{color:var(--blue-dark)}
.feature-lead{left:681px;top:2902px;width:430px;font-size:16.5px;line-height:28px;color:var(--text)}
.check{position:absolute;left:679px;width:430px;padding-left:32px;font-size:16.5px;line-height:28px;color:var(--text)}
.check svg{position:absolute;left:0;top:5px}
/* cards */
.card{position:absolute;top:3412px;width:236px;height:300px;background:var(--white);border-radius:60px 0 60px 0;border-top:2px solid var(--blue-pale);border-right:3px solid var(--blue-light);box-shadow:0 10px 20px rgba(0,84,170,.10);padding:118px 24px 0 26px}
.card h4{font-size:18px;font-weight:600;margin-bottom:8px}
.card .bar{width:30px;height:2px;background:var(--blue);margin:0 0 14px 28px}
.card p{font-size:15.5px;line-height:28px;color:var(--text)}
.card .ico{position:absolute;left:26px;top:48px;width:50px;height:48px;border:2px solid var(--blue-light);border-radius:6px}
.card.featured{background:var(--blue-dark);color:var(--white);border-right-color:var(--blue-pale)}
.card.featured p{color:var(--white)}
.card.featured .bar{background:var(--white)}
.card.featured .ico{border-color:var(--white)}
/* cta */
.cta-band{left:0;top:3797px;width:1200px;height:506px;background:var(--blue-dark);clip-path:polygon(0 47px,100% 0,100% 100%,0 100%)}
/* footer */
.foot-h{font-size:19px;font-weight:600}
.foot-link{position:absolute;font-size:15.5px;color:var(--text)}
.social{position:absolute;top:4455px;width:48px;height:48px;border-radius:50%;background:var(--blue-dark)}
</style>
</head>
<body>

<header class="nav">
  <div class="abs brand" style="left:93px;top:22px"><span class="brand-dot"></span>nubecta</div>
  <a class="active" style="left:403px">Home</a>
  <a style="left:492px">Soluciones</a>
  <a style="left:620px">Prices</a>
  <a style="left:709px">Contact Us</a>
  <a class="btn" style="left:842px;top:27px;width:117px;height:40px;background:var(--blue-dark);font-size:16px">Sign In</a>
  <a class="btn" style="left:971px;top:27px;width:136px;height:40px;background:var(--blue-light);font-size:16px">Free Trial</a>
</header>

<section>
  <div class="abs hero-photo" role="img" aria-label="Photo of hands typing on a keyboard, desaturated"></div>
  <div class="abs hero-kicker">All in one Software</div>
  <h1 class="abs hero-title">Platform to run<br>your business.</h1>
  <a class="btn" style="left:93px;top:457px;width:180px;height:51px;background:var(--blue-light);font-size:18px">Free Trial</a>
</section>

<section>
  <h2 class="abs sec-title" style="top:748px">Featured <span>apps</span></h2>
  <div class="app" style="left:122px;top:840px;border-color:#f0a04b;color:var(--blue-dark)"><i style="background:#f08a2c"></i>VENTAS</div>
  <div class="app" style="left:365px;top:840px;border-color:#8fc0e8;color:var(--blue-dark)"><i style="background:#6fa8d9"></i>COMPRAS</div>
  <div class="app" style="left:608px;top:840px;border-color:#c86ad0;color:var(--blue-dark)"><i style="background:#b05cc4"></i>CONTABILIDAD</div>
  <div class="app" style="left:851px;top:840px;border-color:#d64b55;color:var(--blue-dark)"><i style="background:#d33c48"></i>INVENTARIOS</div>
  <div class="app" style="left:122px;top:951px;border-color:#777;color:var(--blue-dark)"><i style="background:#555"></i>BANCOS</div>
  <div class="app" style="left:365px;top:951px;border-color:#2ea86a;color:#2ea86a"><i style="background:#2ea86a"></i>PRESUPUESTO</div>
  <div class="app" style="left:608px;top:951px;border-color:#52b5a8;color:var(--blue-dark)"><i style="background:#3aa597"></i>NÓMINA RH</div>
  <div class="app" style="left:851px;top:951px;border-color:#6f5bd8;color:var(--blue-dark)"><i style="background:#5a49c9"></i>CRM</div>
</section>

<section>
  <div class="abs" style="left:0;top:1130px;width:140px;height:140px;border-radius:50%;background:var(--blue-mist)"></div>
  <div class="abs profile-band"></div>
  <h2 class="abs sec-title" style="top:1287px;color:var(--white)">Is it to perfil?</h2>
  <div class="mini-hex" style="left:92px;top:1462px;width:46px;height:40px;background:var(--blue-pale)"></div>
  <div class="mini-hex" style="left:132px;top:1484px;width:68px;height:60px;background:var(--white)"></div>
  <div class="mini-hex" style="left:918px;top:1462px;width:46px;height:40px;background:var(--white)"></div>
  <div class="mini-hex" style="left:955px;top:1484px;width:68px;height:60px;background:var(--blue-pale)"></div>

  <div class="hex" style="left:408px;top:1396px"><h3>Profesional</h3><p>Lorem ipsum dolor sit amet sed consectetur adipisicing elit sed do eiusmod tempor incididunt ut labore et dolore magna aliqua.Ut enim ad minim veniam quis nostrud exercitation</p><a>More Information →</a></div>
  <div class="hex" style="left:94px;top:1576px"><h3>Contador</h3><p>Lorem ipsum dolor sit amet sed consectetur adipisicing elit sed do eiusmod tempor incididunt ut labore et dolore magna aliqua.Ut enim ad minim veniam quis nostrud exercitation</p><a>More Information →</a></div>
  <div class="hex" style="left:722px;top:1576px"><h3>PYME</h3><p>Lorem ipsum dolor sit amet sed consectetur adipisicing elit sed do eiusmod tempor incididunt ut labore et dolore magna aliqua.Ut enim ad minim veniam quis nostrud exercitation</p><a>More Information →</a></div>
  <div class="hex" style="left:94px;top:1938px"><h3>Micro</h3><p>Lorem ipsum dolor sit amet sed consectetur adipisicing elit sed do eiusmod tempor incididunt ut labore et dolore magna aliqua.Ut enim ad minim veniam quis nostrud exercitation</p><a>More Information →</a></div>
  <div class="hex" style="left:722px;top:1938px"><h3>Empresarial</h3><p>Lorem ipsum dolor sit amet sed consectetur adipisicing elit sed do eiusmod tempor incididunt ut labore et dolore magna aliqua.Ut enim ad minim veniam quis nostrud exercitation</p><a>More Information →</a></div>
  <div class="mini-hex" style="left:408px;top:1757px;width:382px;height:330px;background:var(--blue-light)"></div>
  <div class="abs" style="left:400px;top:1790px;width:400px;height:560px;border-radius:190px 190px 40px 40px;background:linear-gradient(180deg,#b98a6a 0%,#7a4a3a 30%,#8c8f98 55%,#2c3e66 85%,#e8e8ea 100%)" role="img" aria-label="Photo of a smiling young man sitting cross-legged with a laptop"></div>
</section>

<section>
  <h2 class="abs sec-title" style="top:2493px">Main <span>features</span></h2>
  <div class="abs tabs">
    <div class="tab active"><i></i>Smart Chart of Accounts</div>
    <div class="tab"><i></i>Process 1000 Bills 60 Seconds</div>
    <div class="tab"><i></i>Other Features Goes Here</div>
    <div class="tab"><i></i>Other Features Goes Here</div>
  </div>

  <div class="abs" style="left:0;top:3020px;width:180px;height:260px;border-radius:0 130px 130px 0;background:var(--blue-mist)"></div>
  <svg class="abs" style="left:91px;top:2810px" width="535" height="423" viewBox="0 0 535 423" aria-label="Accounting dashboard with table and charts">
    <rect x="0" y="0" width="535" height="423" rx="8" fill="#fff" stroke="#e3e8ef"/>
    <rect x="0" y="0" width="535" height="24" rx="8" fill="#eef1f5"/>
    <circle cx="14" cy="12" r="4" fill="#ef5f57"/><circle cx="27" cy="12" r="4" fill="#f6bd2e"/><circle cx="40" cy="12" r="4" fill="#28c840"/>
    <rect x="175" y="7" width="200" height="10" rx="5" fill="#fff"/>
    <rect x="0" y="24" width="535" height="20" fill="var(--blue-dark)"/>
    <g fill="#e7ebf0">
      <rect x="10" y="78" width="515" height="8"/><rect x="10" y="94" width="515" height="4"/><rect x="10" y="110" width="515" height="4"/><rect x="10" y="126" width="515" height="4"/><rect x="10" y="142" width="515" height="4"/><rect x="10" y="158" width="515" height="4"/><rect x="10" y="174" width="515" height="4"/><rect x="10" y="190" width="515" height="4"/><rect x="10" y="206" width="515" height="4"/><rect x="10" y="222" width="515" height="4"/><rect x="10" y="238" width="515" height="4"/><rect x="10" y="254" width="515" height="4"/>
    </g>
    <line x1="10" y1="400" x2="400" y2="400" stroke="#dde2e8"/>
    <g>
      <rect x="30" y="370" width="8" height="30" fill="#f08a2c"/><rect x="42" y="340" width="8" height="60" fill="#c9462c"/><rect x="54" y="320" width="8" height="80" fill="#f08a2c"/><rect x="66" y="350" width="8" height="50" fill="#5a49c9"/>
      <rect x="95" y="330" width="8" height="70" fill="#f08a2c"/><rect x="107" y="360" width="8" height="40" fill="#c9462c"/><rect x="119" y="345" width="8" height="55" fill="#5a49c9"/>
      <rect x="150" y="335" width="8" height="65" fill="#f08a2c"/><rect x="162" y="318" width="8" height="82" fill="#c9462c"/><rect x="174" y="360" width="8" height="40" fill="#5a49c9"/>
      <rect x="205" y="325" width="8" height="75" fill="#f08a2c"/><rect x="217" y="350" width="8" height="50" fill="#c9462c"/><rect x="229" y="340" width="8" height="60" fill="#5a49c9"/>
      <rect x="260" y="330" width="8" height="70" fill="#f08a2c"/><rect x="272" y="355" width="8" height="45" fill="#c9462c"/><rect x="284" y="322" width="8" height="78" fill="#5a49c9"/>
      <rect x="315" y="345" width="8" height="55" fill="#f08a2c"/><rect x="327" y="330" width="8" height="70" fill="#c9462c"/><rect x="339" y="360" width="8" height="40" fill="#5a49c9"/>
      <rect x="370" y="338" width="8" height="62" fill="#f08a2c"/><rect x="382" y="352" width="8" height="48" fill="#5a49c9"/>
    </g>
    <circle cx="484" cy="350" r="32" fill="none" stroke="#5a49c9" stroke-width="14"/>
    <circle cx="484" cy="350" r="32" fill="none" stroke="#f6bd2e" stroke-width="14" stroke-dasharray="80 201"/>
    <circle cx="484" cy="350" r="32" fill="none" stroke="var(--blue)" stroke-width="14" stroke-dasharray="40 201" stroke-dashoffset="-80"/>
    <circle cx="484" cy="350" r="32" fill="none" stroke="#f08a2c" stroke-width="14" stroke-dasharray="30 201" stroke-dashoffset="-120"/>
  </svg>

  <h3 class="abs feature-title">Need Smart charts of<br><span>accounts</span></h3>
  <p class="abs feature-lead">Lorem ipsum dolor sit amet consectetur cingy anicy adipisicingy elit sed do eiusmod tempor utterich.</p>
  <div class="check" style="top:2983px"><svg width="18" height="18" viewBox="0 0 18 18"><circle cx="9" cy="9" r="9" fill="var(--blue-dark)"/><path d="M5 9.5l2.6 2.5L13 6.5" stroke="#fff" stroke-width="2" fill="none"/></svg>Excepteur sint occaecat cupidatat non proident sunt in culpa qui officia deserunt mollit anim.</div>
  <div class="check" style="top:3063px"><svg width="18" height="18" viewBox="0 0 18 18"><circle cx="9" cy="9" r="9" fill="var(--blue-dark)"/><path d="M5 9.5l2.6 2.5L13 6.5" stroke="#fff" stroke-width="2" fill="none"/></svg>Ut labore et dolore magnam aliquam quaerat voluptatem.Sunt in culpa qui officia deserunt.</div>
  <div class="check" style="top:3142px"><svg width="18" height="18" viewBox="0 0 18 18"><circle cx="9" cy="9" r="9" fill="var(--blue-dark)"/><path d="M5 9.5l2.6 2.5L13 6.5" stroke="#fff" stroke-width="2" fill="none"/></svg>Duis aute irure dolor in reprehenderit in volupta velit esse cillum dolore eu fugiat nulla incidunt</div>
  <a class="btn" style="left:681px;top:3236px;width:180px;height:50px;background:var(--blue);font-size:18px">Free Trial</a>
</section>

<section>
  <div class="card" style="left:93px"><span class="ico"></span><h4>Page Por Uso</h4><div class="bar"></div><p>Page solo por las funcionalidades que te interesan</p></div>
  <div class="card featured" style="left:350px"><span class="ico"></span><h4>Sin Contrato</h4><div class="bar"></div><p>Page solo por las funcionalidades que te interesan</p></div>
  <div class="card" style="left:610px"><span class="ico" style="border-radius:24px"></span><h4>En La Nube</h4><div class="bar"></div><p>Page solo por las funcionalidades que te interesan</p></div>
  <div class="card" style="left:868px"><span class="ico"></span><h4>Multiples Dispositivos</h4><div class="bar"></div><p>Page solo por las funcionalidades que te interesan</p></div>
</section>

<section>
  <div class="abs cta-band"></div>
  <p class="abs" style="left:93px;top:3945px;font-size:21px;color:var(--white)">What are you waiting for</p>
  <h2 class="abs" style="left:93px;top:3990px;font-size:37px;line-height:52px;font-weight:600;color:var(--white)">To create onefree<br>account In Nubecta</h2>
  <a class="btn" style="left:93px;top:4107px;width:275px;height:50px;background:var(--blue-light);font-size:18px">Crear Cuenta Gratis</a>
  <div class="abs" style="left:604px;top:3892px;width:504px;height:341px;border-radius:30px;background:var(--blue-light)"></div>
  <div class="abs" style="left:595px;top:3884px;width:503px;height:341px;border-radius:30px;background:linear-gradient(135deg,#8a5a1e 0%,#c68a3a 35%,#3d3226 65%,#1f1b18 100%)" role="img" aria-label="Photo of a person in a mustard sweater typing on a laptop"></div>
</section>

<footer>
  <div class="abs brand" style="left:93px;top:4370px"><span class="brand-dot"></span>nubecta</div>
  <span class="social" style="left:92px"></span><span class="social" style="left:149px"></span><span class="social" style="left:205px"></span>

  <div class="abs foot-h" style="left:361px;top:4360px">Quick Links</div>
  <a class="foot-link" style="left:361px;top:4405px">Home</a>
  <a class="foot-link" style="left:361px;top:4438px">Soluciones</a>
  <a class="foot-link" style="left:361px;top:4470px">Prices</a>
  <a class="foot-link" style="left:361px;top:4503px">Contact Us</a>

  <div class="abs foot-h" style="left:552px;top:4360px">Contact info</div>
  <svg class="abs" style="left:552px;top:4410px" width="20" height="22" viewBox="0 0 20 22"><path d="M10 21s7-7 7-12a7 7 0 0 0-14 0c0 5 7 12 7 12z" fill="none" stroke="var(--blue-dark)" stroke-width="1.8"/><circle cx="10" cy="9" r="2.5" fill="none" stroke="var(--blue-dark)" stroke-width="1.8"/></svg>
  <p class="foot-link" style="left:586px;top:4405px;line-height:22px">tempor inci incidi ut<br>labore et dolore</p>
  <svg class="abs" style="left:552px;top:4462px" width="20" height="20" viewBox="0 0 20 20"><path d="M4 2l3 0 2 5-2 1.5a10 10 0 0 0 4.5 4.5L13 11l5 2v3a2 2 0 0 1-2 2A15 15 0 0 1 2 4a2 2 0 0 1 2-2z" fill="none" stroke="var(--blue-dark)" stroke-width="1.7"/></svg>
  <p class="foot-link" style="left:586px;top:4460px">123-456-7890</p>
  <svg class="abs" style="left:552px;top:4504px" width="20" height="16" viewBox="0 0 20 16"><rect x="1" y="1" width="18" height="14" rx="2" fill="none" stroke="var(--blue-dark)" stroke-width="1.7"/><path d="M1 3l9 6 9-6" fill="none" stroke="var(--blue-dark)" stroke-width="1.7"/></svg>
  <p class="foot-link" style="left:586px;top:4500px">info@nubecta.com</p>

  <div class="abs foot-h" style="left:824px;top:4360px">Newsletter</div>
  <div class="abs" style="left:824px;top:4410px;width:282px;height:46px;border-radius:23px;background:var(--blue-mist);padding:12px 22px;font-size:15px;color:var(--text)">Email Address..</div>
  <a class="btn" style="left:824px;top:4472px;width:282px;height:47px;background:var(--blue-dark);font-size:17px">Subscribe !</a>

  <div class="abs" style="left:0;top:4619px;width:1200px;height:1px;background:#e2e6ec"></div>
  <p class="abs" style="left:0;top:4636px;width:1200px;text-align:center;font-size:14px;color:var(--text)">© 2022 Nubecta. All Rights Reserved</p>
</footer>

</body>
</html>
```